Kelvane Plumbing Business cards

Company is Kelvane Plumbing.
name Dashel Morrowby, I am a plumber, drainer, gasfitter and roofer
Mobile: 0431 906 154
Email address: info@kelvaneplumbing.example (check out my website for some ideas)
Website: www.kelvaneplumbing.example
ABN: 82 916 203 471
LIC: 604517K

I am reliable all round plumber. I am a 24 hour emergency service. Kelvane Plumbing is a professional plumbing service in the Harrowvale, Eastern Coast, Northern Brindle and Upper Corran Valley regions of Westmere. We offer a 24 hour emergency service for piece of mind to our customers. Call us now to see how we can help you. Kelvane Plumbing approaches every job with attention to detail and excellent customer service. With our superior workmanship you can be confident that the job will be done right the first time around. You can rest assured with results that are guaranteed to last.

Target Market(s)

the general public

Contact Information for Business Card

look up website for some ideas something with similar colours to logo and new modern and to catch the eye.

Colors
fdfdfd
ffffff
000000
7f7f7f
aaaaaa
33a6d7
0492cd

Requirements
Must have
• all contact details
• company- Kelvane Plumbing
• name- Dashel Morrowby
• number mobile- 0431 906 154
• Email address- info@kelvaneplumbing.example
• Website- www.kelvaneplumbing.example
• ABN- 82 916 203 471
• LIC- 604517K

```html
<!DOCTYPE html>
<html lang="en">
<head>
<meta charset="utf-8">
<title>Kelvane Plumbing – Business Cards</title>
<link rel="stylesheet" href="https://fonts.googleapis.com/css2?family=Hind:wght@400;500;600&display=swap">
<style>
  :root {
    --page: #ffffff;
    --card: #f1f1f1;
    --blue: #0492cd;
    --blue-soft: #33a6d7;
    --ink: #000000;
    --grey: #7f7f7f;
    --grey-light: #aaaaaa;
    --pattern: rgba(51,166,215,0.16);
  }
  * { margin: 0; padding: 0; box-sizing: border-box; }
  html, body { width: 1200px; height: 1200px; overflow: hidden; background: var(--page); }
  body { position: relative; font-family: "Hind", sans-serif; color: var(--ink); }

  .card {
    position: absolute;
    left: 248px;
    width: 711px;
    height: 477px;
    background: var(--card);
    overflow: hidden;
  }
  .card--front { top: 44px; }
  .card--back { top: 687px; }

  .pattern-band {
    position: absolute;
    left: 0; right: 0; bottom: 0;
    background: linear-gradient(to bottom, rgba(51,166,215,0) 0%, var(--pattern) 100%);
  }
  .card--front .pattern-band { height: 230px; }
  .card--back .pattern-band { height: 200px; }

  .brand-name {
    position: absolute;
    color: var(--blue);
    font-weight: 600;
    letter-spacing: 1px;
    white-space: nowrap;
  }
  .card--front .brand-name {
    top: 0; left: 0; width: 100%;
    line-height: 477px;
    text-align: center;
    font-size: 34px;
    margin-top: -2px;
  }
  .card--back .brand-name {
    left: 402px; top: 82px;
    font-size: 25px;
  }

  .holder { position: absolute; left: 62px; top: 76px; }
  .holder__name { font-size: 27px; font-weight: 600; color: var(--blue); letter-spacing: 1.2px; line-height: 1; }
  .holder__role { font-size: 21px; font-weight: 400; color: var(--ink); letter-spacing: 1.2px; line-height: 1; margin-top: 2px; }

  .contact {
    position: absolute;
    display: flex;
    align-items: center;
    gap: 12px;
    font-size: 14px;
    line-height: 16.5px;
    letter-spacing: 0.5px;
    white-space: nowrap;
  }
  .contact svg { flex: none; width: 22px; height: 22px; }
  .contact--web { left: 66px; top: 245px; }
  .contact--mail { left: 360px; top: 245px; }
  .contact--phone { left: 66px; top: 287px; }
  .contact--area { left: 360px; top: 287px; }

  .tagline {
    position: absolute;
    left: 0; width: 100%; top: 382px;
    text-align: center;
    color: var(--blue);
    font-size: 21px;
    font-weight: 500;
    letter-spacing: 1.4px;
    line-height: 24px;
  }
</style>
</head>
<body>

<section class="card card--front">
  <div class="pattern-band" role="img" aria-label="Faint repeating pattern of crossed pipe wrenches"></div>
  <div class="brand-name">KELVANE PLUMBING</div>
</section>

<section class="card card--back">
  <div class="pattern-band" role="img" aria-label="Faint repeating pattern of crossed pipe wrenches"></div>

  <div class="holder">
    <p class="holder__name">DASHEL MORROWBY</p>
    <p class="holder__role">OWNER</p>
  </div>

  <div class="brand-name">KELVANE PLUMBING</div>

  <div class="contact contact--web">
    <svg viewBox="0 0 24 24" fill="none" stroke="var(--blue)" stroke-width="1.6">
      <circle cx="12" cy="12" r="10"/>
      <ellipse cx="12" cy="12" rx="4.5" ry="10"/>
      <line x1="2" y1="12" x2="22" y2="12"/>
      <line x1="4" y1="7" x2="20" y2="7"/>
      <line x1="4" y1="17" x2="20" y2="17"/>
      <line x1="12" y1="2" x2="12" y2="22"/>
    </svg>
    <span>www.kelvaneplumbing.example</span>
  </div>

  <div class="contact contact--mail">
    <svg viewBox="0 0 24 24" fill="none" stroke="var(--blue)" stroke-width="1.8">
      <rect x="2" y="5" width="20" height="14"/>
      <polyline points="2,5 12,13 22,5"/>
      <line x1="2" y1="19" x2="9.5" y2="11"/>
      <line x1="22" y1="19" x2="14.5" y2="11"/>
    </svg>
    <span>info@kelvaneplumbing.example</span>
  </div>

  <div class="contact contact--phone">
    <svg viewBox="0 0 24 24" fill="none" stroke="var(--blue)" stroke-width="1.7" stroke-linejoin="round">
      <path d="M6 3l3.5 4-2 2.5c1.3 3 3.8 5.5 7 7l2.5-2 4 3.5-2.5 3C11 21 3 13 3 5.5z"/>
    </svg>
    <span>Mobile : 0431 906 154<br>ABN : 82 916 203 471<br>LIC : 604517K</span>
  </div>

  <div class="contact contact--area">
    <svg viewBox="0 0 24 24" fill="none" stroke="var(--blue)" stroke-width="1.7">
      <path d="M12 22s-7-7.5-7-12.5a7 7 0 0 1 14 0C19 14.5 12 22 12 22z"/>
      <circle cx="12" cy="9.5" r="2.6"/>
    </svg>
    <span>Harrowvale, Eastern Coast, Northern<br>Brindle and Upper Corran Valley regions<br>of Westmere</span>
  </div>

  <p class="tagline">24 HOUR EMERGENCY SERVICE<br>ONE STOP PLUMBING</p>
</section>

</body>
</html>
```